"Oral Surgery Office needs a Business Card Design with Logo"

We need a logo design and business card. The name of the office is Halvering Oral Surgery & Implant Center. The final design should communicate uniqueness as well as highly class office. The business card should emphasize power. I included the current business card below. Please design something unique

Target Market(s)

Dentists & Patients

Industry/Entity Type

Dental

Contact Information for Business Card

Unique Design to show success, prestige, Style, unmatched performance

Font styles to use
Serif

Colors
1b1b1b
ffffff
0556a4

Requirements
Must have
• Bussiness Name, Doctor's Name, Website, phone and Fax, email, office address
• Color should be either Black and White or Blue and White
Nice to have
• Clean look
Should not have
• the business card shouldn't be too busy. I feel like the old business card was too busy

```html
<!DOCTYPE html>
<html lang="en">
<head>
<meta charset="utf-8">
<title>Halvering Oral Surgery &amp; Implant Center — Business Card</title>
<link href="https://fonts.googleapis.com/css2?family=Montserrat:wght@300;400&display=swap" rel="stylesheet">
<style>
  :root {
    --backdrop: #93e0c8;
    --card: #f4f4f3;
    --brand-blue: #1a6fb5;
    --blue-top: #1a72b8;
    --blue-mid: #86b6d8;
    --blue-bottom: #33b2de;
    --text-grey: #8d8d8d;
    --white: #ffffff;
  }
  * { margin: 0; padding: 0; box-sizing: border-box; }
  html, body {
    width: 1200px; height: 1200px; overflow: hidden;
    background: var(--backdrop);
    font-family: "Montserrat", sans-serif;
  }
  .card {
    position: absolute; left: 180px;
    width: 840px; height: 480px;
    background: var(--card);
    box-shadow: 0 6px 18px rgba(0,0,0,0.12);
    overflow: hidden;
  }
  .card--front { top: 90px; }
  .card--back { top: 630px; }

  .brand-panel {
    position: absolute; left: 0; top: 0; bottom: 0; width: 330px;
    background: linear-gradient(180deg, var(--blue-top) 0%, var(--blue-mid) 55%, var(--blue-bottom) 85%, var(--blue-bottom) 100%);
    display: flex; flex-direction: column; align-items: center; justify-content: center;
    gap: 26px;
  }
  .brand-mark {
    width: 90px; height: 90px; border-radius: 50%;
    background: rgba(255,255,255,0.9);
  }
  .brand-name {
    color: var(--white); font-weight: 300; text-align: center;
    font-size: 15px; letter-spacing: 0.12em; line-height: 1.6;
    text-transform: uppercase;
  }
  .details {
    position: absolute; left: 380px; top: 0; bottom: 0; right: 40px;
  }
  .doctor-name {
    position: absolute; top: 92px;
    color: var(--brand-blue); font-weight: 400; font-size: 23px;
  }
  .doctor-specialty {
    position: absolute; top: 128px;
    color: var(--text-grey); font-weight: 300; font-size: 20px;
  }
  .contact {
    position: absolute; bottom: 52px;
    color: var(--text-grey); font-weight: 300; font-size: 15px; line-height: 1.5;
  }
  .contact__web { color: var(--brand-blue); font-weight: 400; }

  .back-lockup {
    position: absolute; inset: 0;
    display: flex; flex-direction: column; align-items: center; justify-content: center;
    gap: 34px;
  }
  .back-mark {
    width: 170px; height: 170px; border-radius: 50%;
    background: var(--brand-blue); opacity: 0.75;
  }
  .back-name {
    color: var(--brand-blue); font-weight: 300; text-align: center;
    text-transform: uppercase; letter-spacing: 0.1em;
    font-size: 26px; line-height: 1.5;
  }
</style>
</head>
<body>
  <section class="card card--front">
    <div class="brand-panel">
      <div class="brand-mark"></div>
      <p class="brand-name">Halvering<br>Oral Surgery &amp; Implant Center</p>
    </div>
    <div class="details">
      <h1 class="doctor-name">Dr. Marcus Velden, D.D.S.</h1>
      <p class="doctor-specialty">Oral &amp; Maxillofacial Surgery</p>
      <p class="contact">
        2840 Linden Row Halvering, NY 10482<br>
        Tel: 555-204-3100 Fax: 555-204-3106<br>
        email: HalveringOralSurgeon@mailbox.com<br>
        <span class="contact__web">www.HalveringOralSurgeryCenter.com</span>
      </p>
    </div>
  </section>

  <section class="card card--back">
    <div class="back-lockup">
      <div class="back-mark"></div>
      <p class="back-name">Halvering<br>Oral Surgery &amp; Implant Center</p>
    </div>
  </section>
</body>
</html>
```